Car Soap Label Design specifically targeting RVs

I am private labeling a car wash soap to specifically target the RV industry. It will be sold in a one gallon jug with a 6"x11" spot to place the label on front and wrap around the two sides. (see attached pics for example of label size) The front of the label I want to have a realistic picture of a high dollar class A RV somehow integrated into the design, and the key features of the soap. I had wordsmithbot design a couple that I kind of like the look of that I will attach, but open to other options. I want something clean and professional looking that will back the premium product I am selling.
The name of my brand is "Blue Harbor Gleam". I want the brand name to be somewhere on the label, but not a main focus. I want the focus to be the product and its benefits. "Premium RV Wash and Wax" as the main verbiage. Benefits... "Developed for Use With Foam Gun or Bucket with Water", "Safe for All RV Exteriors", "Protective Wax Formula", "Enhanced Shine", "Water Repellent", "Streak Free Rinse", "UV Protection". On the side...Directions: 2 Ways of Mixing... Pour Concentrate into Foam Gun Bottle OR Mixing Ratio: 1 Part Wash & Wax / 3 Parts Water in bucket. Apply soap to one side of RV at a time and use carwash brush to easily loosen road film and rinse clean. On the other side... Keep from freezing, Keep Out of Reach of Children. MADE IN USA. Hazardous Ingredients: NONE . NOTICE: The seller and/or manufacturer assumes no responsibility for damage or injury resulting from misuse of this product. No warranties, expressed or implied, are given for the performance or safety of this product.

Target Market(s)

RV industry

Industry/Entity Type

RV/Auto

Requirements
Must have
• Clean, Professional look, size 6" tall and 11" wide
Nice to have
• Realistic Class A RV as part of design

```html
<!DOCTYPE html>
<html lang="en">
<head>
<meta charset="utf-8">
<title>Premium RV Wash and Wax – Label</title>
<link href="https://fonts.googleapis.com/css2?family=Montserrat:wght@500;600;700;800;900&family=Arimo:wght@400;700&display=swap" rel="stylesheet">
<style>
  :root {
    --page-bg: #e6e8ea;
    --label-steel: #6e8a9f;
    --label-steel-light: #9fb3c2;
    --label-steel-dark: #4c6477;
    --band-navy: #2a3a7c;
    --band-navy-dark: #1f2c66;
    --title-outline: #1d3f8f;
    --white: #ffffff;
    --brand-red: #c8202a;
    --ink-soft: #eef3f7;
  }
  * { box-sizing: border-box; margin: 0; padding: 0; }
  html, body { width: 1200px; height: 900px; overflow: hidden; }
  body {
    background: var(--page-bg);
    font-family: "Montserrat", sans-serif;
    position: relative;
  }
  .label-set {
    position: absolute;
    left: 105px;
    top: 268px;
    display: flex;
    gap: 40px;
  }
  .label {
    position: relative;
    height: 364px;
    overflow: hidden;
    box-shadow: 0 6px 18px rgba(0,0,0,0.12);
  }
  .label-backdrop {
    position: absolute;
    inset: 0;
    background: linear-gradient(180deg, var(--label-steel-light) 0%, var(--label-steel) 45%, var(--label-steel-dark) 100%);
  }
  .bottom-band {
    position: absolute;
    left: 0; right: 0; bottom: 0;
    height: 88px;
    background: linear-gradient(180deg, var(--band-navy) 0%, var(--band-navy-dark) 100%);
  }

  /* Front panel */
  .front-panel { width: 640px; }
  .brand-tab {
    position: absolute;
    top: 0; right: 0;
    width: 300px; height: 30px;
    background: var(--white);
    clip-path: polygon(0 0, 100% 0, 100% 100%, 30px 100%);
    display: flex; align-items: center; justify-content: center;
    padding-left: 26px;
  }
  .brand-name {
    font-family: "Montserrat", sans-serif;
    font-weight: 800;
    font-size: 15px;
    color: var(--brand-red);
    text-transform: uppercase;
    letter-spacing: 0.2px;
  }
  .product-title {
    position: absolute;
    left: 34px; top: 42px;
    width: 320px;
    text-align: center;
    font-weight: 900;
    font-size: 29px;
    line-height: 1.05;
    color: var(--white);
    text-transform: uppercase;
    text-shadow:
      2px 0 0 var(--title-outline), -2px 0 0 var(--title-outline),
      0 2px 0 var(--title-outline), 0 -2px 0 var(--title-outline),
      2px 2px 0 var(--title-outline), -2px -2px 0 var(--title-outline),
      2px -2px 0 var(--title-outline), -2px 2px 0 var(--title-outline),
      3px 4px 4px rgba(0,0,0,0.35);
  }
  .benefit-list {
    position: absolute;
    left: 60px; top: 138px;
    list-style: none;
  }
  .benefit-list li {
    display: flex; align-items: center; gap: 6px;
    font-weight: 500;
    font-size: 16.5px;
    color: var(--ink-soft);
    height: 24.5px;
  }
  .tick-icon { width: 15px; height: 15px; flex: none; }
  .usage-note {
    position: absolute;
    left: 30px; bottom: 22px;
    width: 290px;
    text-align: center;
    font-weight: 700;
    font-size: 10.5px;
    line-height: 1.4;
    color: var(--white);
    text-transform: uppercase;
  }
  .rv-photo {
    position: absolute;
    left: 318px; top: 60px;
    width: 322px; height: 272px;
    background:
      radial-gradient(ellipse at 45% 60%, #3b3631 0%, #2b2825 45%, rgba(80,92,104,0) 75%),
      linear-gradient(180deg, rgba(150,165,178,0) 0%, rgba(60,66,72,0.35) 100%);
  }
  .gallon-badge {
    position: absolute;
    left: 578px; top: 284px;
    width: 40px; height: 40px;
    border-radius: 50%;
    background: var(--brand-red);
    border: 2px solid var(--white);
    color: var(--white);
    display: flex; flex-direction: column; align-items: center; justify-content: center;
    font-weight: 800;
    line-height: 1;
  }
  .gallon-badge .qty { font-size: 15px; }
  .gallon-badge .unit { font-size: 5.5px; letter-spacing: 0.5px; margin-top: 1px; }

  /* Side panel */
  .side-panel { width: 310px; }
  .side-title {
    position: absolute;
    left: 0; right: 0; top: 20px;
    text-align: center;
    font-weight: 900;
    font-size: 17px;
    line-height: 1.05;
    color: var(--white);
    text-transform: uppercase;
    text-shadow:
      1.5px 0 0 var(--title-outline), -1.5px 0 0 var(--title-outline),
      0 1.5px 0 var(--title-outline), 0 -1.5px 0 var(--title-outline),
      2px 2px 3px rgba(0,0,0,0.3);
  }
  .side-copy {
    position: absolute;
    left: 26px; right: 26px; top: 74px;
    font-family: "Arimo", sans-serif;
    font-size: 8.6px;
    line-height: 1.32;
    color: var(--ink-soft);
    text-align: justify;
  }
  .side-copy p { margin-bottom: 16px; }
  .side-copy strong { font-weight: 700; text-transform: uppercase; }
  .care-row {
    position: absolute;
    left: 0; right: 0; bottom: 46px;
    display: flex; justify-content: center; gap: 22px;
  }
  .care-item {
    display: flex; align-items: center; gap: 6px;
    font-family: "Arimo", sans-serif;
    font-weight: 700;
    font-size: 7.5px;
    line-height: 1.15;
    color: var(--white);
    text-transform: uppercase;
  }
  .care-icon {
    width: 22px; height: 22px; border-radius: 50%;
    border: 1.5px solid var(--white);
    flex: none;
  }
  .origin-mark {
    position: absolute;
    left: 0; right: 0; bottom: 12px;
    display: flex; justify-content: center; align-items: center; gap: 6px;
    color: var(--white);
  }
  .origin-mark .flag { width: 32px; height: 20px; }
  .origin-text { line-height: 1; font-weight: 800; }
  .origin-text .small { display: block; font-size: 7px; letter-spacing: 0.5px; }
  .origin-text .big { display: block; font-size: 16px; }
</style>
</head>
<body>
  <main class="label-set">
    <section class="label front-panel">
      <div class="label-backdrop" role="img" aria-label="Misty blue-grey mountain landscape background"></div>
      <div class="bottom-band"></div>
      <div class="rv-photo" role="img" aria-label="Photo of a dark luxury Class A motorhome"></div>
      <div class="brand-tab"><span class="brand-name">Blue Harbor Gleam</span></div>
      <h1 class="product-title">Premium RV<br>Wash and Wax</h1>
      <ul class="benefit-list">
        <li><svg class="tick-icon" viewBox="0 0 16 16"><circle cx="8" cy="8" r="6.8" fill="none" stroke="#eef3f7" stroke-width="1.3"/><path d="M4.8 8.2l2.2 2.2 4.3-4.6" fill="none" stroke="#eef3f7" stroke-width="1.5" stroke-linecap="round" stroke-linejoin="round"/></svg>Protective Wax Formula</li>
        <li><svg class="tick-icon" viewBox="0 0 16 16"><circle cx="8" cy="8" r="6.8" fill="none" stroke="#eef3f7" stroke-width="1.3"/><path d="M4.8 8.2l2.2 2.2 4.3-4.6" fill="none" stroke="#eef3f7" stroke-width="1.5" stroke-linecap="round" stroke-linejoin="round"/></svg>Enhanced Shine</li>
        <li><svg class="tick-icon" viewBox="0 0 16 16"><circle cx="8" cy="8" r="6.8" fill="none" stroke="#eef3f7" stroke-width="1.3"/><path d="M4.8 8.2l2.2 2.2 4.3-4.6" fill="none" stroke="#eef3f7" stroke-width="1.5" stroke-linecap="round" stroke-linejoin="round"/></svg>Water Repellent</li>
        <li><svg class="tick-icon" viewBox="0 0 16 16"><circle cx="8" cy="8" r="6.8" fill="none" stroke="#eef3f7" stroke-width="1.3"/><path d="M4.8 8.2l2.2 2.2 4.3-4.6" fill="none" stroke="#eef3f7" stroke-width="1.5" stroke-linecap="round" stroke-linejoin="round"/></svg>Streak Free Rinse</li>
        <li><svg class="tick-icon" viewBox="0 0 16 16"><circle cx="8" cy="8" r="6.8" fill="none" stroke="#eef3f7" stroke-width="1.3"/><path d="M4.8 8.2l2.2 2.2 4.3-4.6" fill="none" stroke="#eef3f7" stroke-width="1.5" stroke-linecap="round" stroke-linejoin="round"/></svg>UV Protection</li>
      </ul>
      <p class="usage-note">Developed for use with foam gun<br>or bucket with water safe for all<br>RV exteriors</p>
      <div class="gallon-badge"><span class="unit">GALLON</span><span class="qty">1</span><span class="unit">GALLON</span></div>
    </section>

    <section class="label side-panel">
      <div class="label-backdrop" role="img" aria-label="Misty blue-grey mountain landscape background"></div>
      <div class="bottom-band"></div>
      <h2 class="side-title">Premium RV<br>Wash and Wax</h2>
      <div class="side-copy">
        <p><strong>Directions:</strong> 2 Ways of Mixing... Pour Concentrate into Foam Gun Bottle OR Mixing Ratio: 1 Part Wash &amp; Wax / 3 Parts Water in bucket. Apply soap to one side of RV at a time and use carwash brush to easily loosen road film and rinse clean.</p>
        <p><strong>Hazardous Ingredients:</strong> NONE.</p>
        <p><strong>Notice:</strong> The seller and/or manufacturer assumes no responsibility for damage or injury resulting from misuse of this product. No warranties, expressed or implied, are given for the performance or safety of this product.</p>
      </div>
      <div class="care-row">
        <div class="care-item"><span class="care-icon"></span><span>Keep out of reach<br>of children</span></div>
        <div class="care-item"><span class="care-icon"></span><span>Keep from<br>freezing</span></div>
      </div>
      <div class="origin-mark">
        <svg class="flag" viewBox="0 0 32 20">
          <rect x="0" y="0" width="32" height="20" fill="none"/>
          <rect x="0" y="0" width="32" height="2.5" fill="#fff"/>
          <rect x="0" y="5.8" width="32" height="2.5" fill="#fff"/>
          <rect x="0" y="11.6" width="32" height="2.5" fill="#fff"/>
          <rect x="0" y="17.4" width="32" height="2.5" fill="#fff"/>
          <rect x="0" y="0" width="12" height="9" fill="#fff"/>
        </svg>
        <span class="origin-text"><span class="small">MADE IN</span><span class="big">USA</span></span>
      </div>
    </section>
  </main>
</body>
</html>
```